Website for a web design agency

We are a website and marketing agency. We do website design, development, and well as Brindle and Quorvia advertising and analytics. We ourselves need a new website for our own brand. We are working on some designs in-house with our own designers, but we also wanted to see what outside designers would come up with.
We are starting off with the homepage, and here is the breakdown of the sections:
https://files.brindlework.example/sheet/d/7kqTr2VnPLwXeHsaMcY4oBfJzuGNtKdWiEh3Rx9pLmQb/view?mode=share
This doc also has many links to sites we have done, which you can take screenshots of for the portfolio section.
In terms of the "look" I am going for, I want to look high-end and very beautiful designs. I found this website that I like a lot that you can use some of the elements of, just as a starting point:
http://velmarkstudio.example/layouts/pixelbarn/html/ostrevo/index.html and here is another design option they have http://velmarkstudio.example/layouts/pixelbarn/html/ostrevo/index-4.html
I'm also uploading my logo. The logo matches the gold and black look from these websites, but I would be open to switching to another color scheme if needed.
This is the link to my very old website, which you can use for some of the dummy text, and a pic of myself. I will be taking more pics of myself:
https://theplumtreeandwillowgroup.example/
We need a homepage and a portfolio page right now, but if you are the winner, we will be hiring you to make additional pages.
Updates
More designs continue to come in even today, and I want to make sure no other designers are still submitting designs.
Target Market(s)
medium and large businesses owners, and non-profits
Number of Pages Required
1 page

```html
<!DOCTYPE html>
<html lang="en">
<head>
<meta charset="utf-8">
<title>Corvane Strategies – Home</title>
<link href="https://fonts.googleapis.com/css2?family=Mulish:ital,wght@0,400;0,600;0,700;0,800;1,400;1,600&display=swap" rel="stylesheet">
<style>
:root{
  --blue:#0a2fdc;
  --blue-light:#1d5ff0;
  --black:#000;
  --white:#fff;
  --green:#1ec27a;
  --gold:#f2b619;
  --red:#ff3b3b;
  --ink:#111;
  --grey:#e9e9ec;
}
*{box-sizing:border-box;margin:0;padding:0}
html,body{width:1200px;height:3125px;overflow:hidden}
body{position:relative;font-family:"Mulish",sans-serif;color:var(--ink);background:var(--white)}
.abs{position:absolute}
.btn{position:absolute;background:var(--green);color:var(--white);font-weight:700;font-size:11px;display:flex;align-items:center;justify-content:center;border-radius:2px}
/* header */
.site-header{position:absolute;left:0;top:0;width:1200px;height:56px;background:var(--black)}
.brand{position:absolute;left:227px;top:17px;color:var(--gold);font-weight:800;font-size:15px;line-height:1}
.brand small{display:block;font-size:6px;letter-spacing:2px;font-weight:700;margin-top:2px}
.nav{position:absolute;top:22px;left:599px;display:flex;gap:0;font-size:11px;color:var(--white)}
.nav span{margin-right:34px}
/* hero */
.hero{position:absolute;left:0;top:56px;width:1200px;height:457px;background:var(--blue)}
.hero h1{position:absolute;left:226px;top:64px;color:var(--white);font-size:36px;font-weight:700}
.hero p{position:absolute;left:226px;top:117px;color:var(--white);font-size:14px;line-height:21px}
.video{position:absolute;left:625px;top:99px;width:350px;height:196px;background:linear-gradient(135deg,#3b3b3b,#5a5a5a 60%,#2e2e2e)}
.video .cap{position:absolute;left:4px;top:128px;color:#bdbdbd;font-size:19px;line-height:20px;letter-spacing:1px}
.video .cap span{display:block;padding-left:32px;font-size:15px}
/* services */
.services{position:absolute;left:226px;top:337px;width:749px;height:282px;background:linear-gradient(#1d56e8,#0f3ce6);border-radius:4px}
.svc{position:absolute;width:200px;text-align:center;color:var(--white);font-size:10px}
.svc svg{display:block;margin:0 auto 8px}
.svc .arr{margin-top:14px}
/* portfolio */
.shot{position:absolute;left:226px;top:676px;width:346px;height:136px;border-top:3px solid var(--green);background:linear-gradient(120deg,#0b1d4a,#1a3c8a 60%,#0b1733)}
.shot-bar{position:absolute;left:0;top:0;width:346px;height:22px;background:var(--white)}
.shot-title{position:absolute;left:0;top:50px;width:346px;text-align:center;color:var(--white);font-size:17px;letter-spacing:1px}
.card{position:absolute;left:226px;top:836px;width:346px;height:189px;background:var(--blue);color:var(--white);padding:22px 20px}
.card h3{font-size:14px;font-weight:700;margin-bottom:6px}
.card p{font-size:9.6px;line-height:15px}
.card a{display:block;margin-top:10px;color:var(--green);font-size:10px;font-weight:700}
.port h2{position:absolute;left:605px;top:703px;font-size:22px;font-weight:700}
.port .lead{position:absolute;left:605px;top:738px;font-size:15px;font-style:italic;line-height:22px}
.port .body{position:absolute;left:605px;top:803px;width:368px;font-size:11px;line-height:17px}
.woman{position:absolute;left:795px;top:932px;width:175px;height:376px;border-radius:80px 80px 0 0;background:linear-gradient(#e8e8ee,#c9d0ea 60%,rgba(60,90,220,.4))}
.dots{position:absolute;display:flex;gap:4px}
.dots i{width:5px;height:5px;border-radius:50%;background:#ccc;display:block}
/* testimonials */
.testi{position:absolute;left:0;top:1082px;width:1200px;height:227px;background:var(--blue);color:var(--white)}
.testi h2{position:absolute;left:234px;top:18px;font-size:25px;font-weight:700}
.testi h3{position:absolute;left:267px;top:56px;font-size:16px;font-weight:700}
.testi .q{position:absolute;left:234px;top:56px;color:var(--red);font-size:30px;font-weight:800;line-height:1}
.testi p{position:absolute;left:268px;top:84px;width:480px;font-size:10.5px;line-height:22.5px;font-style:italic;font-weight:600}
.testi .who{position:absolute;left:268px;top:177px;color:var(--red);font-size:8.5px;font-weight:700}
.testi .woman{top:-150px}
/* build */
.build h2{position:absolute;left:224px;top:1433px;font-size:22px;font-weight:700;line-height:31px}
.build p{position:absolute;left:224px;top:1503px;width:370px;font-size:14px;line-height:21px}
.phone-photo{position:absolute;left:600px;top:1367px;width:600px;height:312px;background:linear-gradient(120deg,#f4f4f6 30%,#d8dbe4 55%,#30323a 62%,#eef0f6 70%,#ffffff)}
/* help */
.help{position:absolute;left:226px;top:1736px;width:749px;height:930px;background:var(--blue);color:var(--white)}
.help h2{position:absolute;font-size:22px;font-weight:700}
.help .t{position:absolute;font-size:11px;line-height:17px}
.col h4{font-size:14px;font-weight:700;margin:12px 0 10px}
.col p{font-size:11px;line-height:17px}
.col a{display:block;margin-top:6px;color:var(--green);font-size:10px;font-weight:700;text-decoration:underline}
.col{position:absolute;width:190px}
.val{position:absolute;width:120px}
.val h5{font-size:9.5px;font-weight:700;margin:10px 0 6px}
.val p{font-size:9px;line-height:12px}
.team-photo{position:absolute;left:53px;top:665px;width:208px;height:208px;background:linear-gradient(#f1f1f1,#e0d9d2)}
.avatar{position:absolute;border-radius:50%}
/* footer */
.footer{position:absolute;left:0;top:2723px;width:1200px;height:347px;background:var(--blue);color:var(--white)}
.fh{position:absolute;font-size:10px;font-weight:700}
.fh::after{content:"";display:block;width:60px;height:1.5px;background:var(--green);margin-top:7px}
.ft{position:absolute;font-size:10.5px;line-height:15px}
.field{position:absolute;background:var(--white);color:#aaa;font-size:9px;padding:9px}
.bottom{position:absolute;left:0;top:3070px;width:1200px;height:55px;background:var(--black);color:var(--white);font-size:9px;font-weight:700}
.soc{position:absolute;top:17px;width:20px;height:20px;border:2px solid var(--white);border-radius:50%}
</style>
</head>
<body>

<header class="site-header">
  <div class="brand">CORVANE<small>STRATEGIES</small></div>
  <nav class="nav"><span>Home</span><span>About</span><span>Service</span><span>Portfolio</span><span>Team</span><span>Contact</span></nav>
</header>

<section class="hero">
  <h1>We build Value</h1>
  <p>Enterprise Level Website Development<br>and Online Marketing.</p>
  <div class="btn" style="left:226px;top:176px;width:125px;height:33px">Get a Quote</div>
</section>
<div class="video" role="img" aria-label="Introductory video still of the agency founder">
  <svg class="abs" style="left:164px;top:86px" width="22" height="22" viewBox="0 0 22 22"><circle cx="11" cy="11" r="9.5" fill="none" stroke="#ddd" stroke-width="1.2"/><path d="M9 7l6 4-6 4z" fill="#ddd"/></svg>
  <div class="cap">Marcus Delane<span>web developer</span></div>
</div>

<section class="services">
  <div class="svc" style="left:30px;top:38px">
    <svg width="32" height="30" viewBox="0 0 32 30" fill="none" stroke="#fff" stroke-width="1.2"><rect x="2" y="2" width="26" height="22"/><path d="M2 7h26M10 14l-3 3 3 3M18 14l3 3-3 3M15 13l-2 8"/></svg>
    Web Design<svg class="arr" width="34" height="12" viewBox="0 0 34 12" fill="none" stroke="#fff" stroke-width="1.5"><path d="M1 6h31M27 1l5 5-5 5"/></svg></div>
  <div class="svc" style="left:290px;top:38px">
    <svg width="24" height="32" viewBox="0 0 24 32" fill="none" stroke="#fff" stroke-width="1.2"><rect x="2" y="2" width="20" height="28"/><path d="M5 7h14M5 12h14M5 17h6M13 17h6M5 22h14"/></svg>
    Landing Pages<svg class="arr" width="34" height="12" viewBox="0 0 34 12" fill="none" stroke="#fff" stroke-width="1.5"><path d="M1 6h31M27 1l5 5-5 5"/></svg></div>
  <div class="svc" style="left:546px;top:38px">
    <svg width="34" height="32" viewBox="0 0 34 32" fill="none" stroke="#fff" stroke-width="1.2"><path d="M3 30V20h5v10M12 30V15h5v15M21 30V18h5v12M29 30V10h4v20"/><path d="M5 12l9-6 9 4 9-8"/></svg>
    Analytics &amp; optimisation<svg class="arr" width="34" height="12" viewBox="0 0 34 12" fill="none" stroke="#fff" stroke-width="1.5"><path d="M1 6h31M27 1l5 5-5 5"/></svg></div>
  <div class="svc" style="left:30px;top:150px">
    <svg width="34" height="30" viewBox="0 0 34 30" fill="none" stroke="#fff" stroke-width="1.2"><rect x="2" y="4" width="24" height="18"/><circle cx="27" cy="6" r="5"/><path d="M12 14v10l3-3 3 5M2 9h24"/></svg>
    PPC &amp; Funnels<svg class="arr" width="34" height="12" viewBox="0 0 34 12" fill="none" stroke="#fff" stroke-width="1.5"><path d="M1 6h31M27 1l5 5-5 5"/></svg></div>
  <div class="svc" style="left:290px;top:150px">
    <svg width="32" height="32" viewBox="0 0 32 32" fill="none" stroke="#fff" stroke-width="1.2"><rect x="2" y="2" width="28" height="28"/><circle cx="16" cy="13" r="6"/><path d="M2 22h28"/></svg>
    Donation Pages<svg class="arr" width="34" height="12" viewBox="0 0 34 12" fill="none" stroke="#fff" stroke-width="1.5"><path d="M1 6h31M27 1l5 5-5 5"/></svg></div>
  <div class="svc" style="left:546px;top:150px">
    <svg width="32" height="32" viewBox="0 0 32 32" fill="none" stroke="#fff" stroke-width="1.2"><rect x="2" y="8" width="28" height="20"/><rect x="11" y="2" width="10" height="6"/><path d="M13 14l7 4-7 4z"/></svg>
    Video Marketing<svg class="arr" width="34" height="12" viewBox="0 0 34 12" fill="none" stroke="#fff" stroke-width="1.5"><path d="M1 6h31M27 1l5 5-5 5"/></svg></div>
</section>

<section class="port">
  <div class="shot" role="img" aria-label="Screenshot of the Ostara Productions website">
    <div class="shot-bar"></div>
    <div class="shot-title">OSTARA PRODUCTIONS</div>
  </div>
  <article class="card">
    <h3>Ostara Productions</h3>
    <p>Ostara Productions is the production company of television writer, producers, and husband-and-wife duo Teo &amp; Lina Varrow that was founded in 2000. It was first known as "Bright Meadow Productions" from 2000 to 2008. The powerhouse duo both write and produce with a focus on developing new and exciting projects for both television and film.</p>
    <a>Read More</a>
  </article>
  <h2>Our Portfolio</h2>
  <p class="lead">These are some of my favorite projects we've<br>done for our clients</p>
  <p class="body">Lorem ipsum dolor sit amet, consectetur adipiscing elit, sed do eiusmod tempor incididunt ut labore et dolore magna aliqua. Quis ipsum suspendisse ultrices gravida. Risus commodo viverra maecenas accumsan lacus vel facilisis. Lorem ipsum dolor sit amet, consectetur adipiscing elit, sed do eiusmod tempor incididunt ut labore et dolore magna aliqua. Quis ipsum suspendisse ultrices gravida. Risus commodo viverra maecenas accumsan lacus vel facilisis.</p>
  <div class="btn" style="left:605px;top:949px;width:113px;height:29px">View Gallery</div>
  <div class="dots" style="left:583px;top:1052px"><i></i><i></i><i></i><i style="background:var(--red)"></i></div>
</section>

<section class="testi">
  <h2>Client Testimonials</h2>
  <div class="q">“</div>
  <h3>Incredible value and peace of mind</h3>
  <p>Corvane strategies Services provide us with insight into the health of our network something we couldn't quantify in the past. The remote monitoring capabilities help us identify small issues before they become major problems and save time and money by anticipating server upgrades. Overall, they provide us with incredible value and peace of mind.</p>
  <div class="who">HAROLD BENNING, LAKEVIEW LENDING FAIRMONT, NJ</div>
  <div class="dots" style="left:268px;top:197px"><i style="background:var(--red)"></i><i style="background:#fff"></i><i style="background:#fff"></i></div>
  <div class="woman" role="img" aria-label="Smiling woman holding a smartphone"></div>
</section>

<section class="build">
  <h2>Let's build your business<br>online, together.</h2>
  <p>I want to build your site or get you higher on Brindle. Unlike big agencies, I want to hold your hand hroughout the process.</p>
  <div class="btn" style="left:224px;top:1577px;width:112px;height:29px">Case Study</div>
  <div class="phone-photo" role="img" aria-label="Close-up of a phone showing search results for analytics"></div>
</section>

<section class="help">
  <h2 style="left:54px;top:52px">How We Help ?</h2>
  <p class="t" style="left:57px;top:81px;width:310px">Whether you are just starting out or already a successful business, having a successful online presence is always a central part of your business.</p>
  <p class="t" style="left:57px;top:148px">Here is how we can help you :</p>

  <div class="col" style="left:57px;top:188px">
    <svg width="34" height="32" viewBox="0 0 34 32" fill="none" stroke="#2ee08c" stroke-width="1.2"><rect x="2" y="2" width="30" height="20"/><circle cx="17" cy="12" r="4"/><path d="M17 22v6M9 30h16"/></svg>
    <h4>Create</h4><p>I can help you figure out what makes you unique. It's your unique selling point that helps you stand out from the other millions.</p><a>Read More</a></div>
  <div class="col" style="left:279px;top:188px">
    <svg width="42" height="32" viewBox="0 0 42 32" fill="none" stroke="#2ee08c" stroke-width="1.2"><rect x="1" y="1" width="40" height="30"/><path d="M1 7h40M6 12h8M6 17h8M6 22h8M18 12h18M18 17h14M18 22h18"/></svg>
    <h4>Build</h4><p>Your website is your own special place online for what you are trying to bring to the world. I help make it stand out for.</p><a>Read More</a></div>
  <div class="col" style="left:498px;top:188px">
    <svg width="20" height="32" viewBox="0 0 20 32" fill="none" stroke="#2ee08c" stroke-width="1.2"><path d="M10 1c6 6 6 16 3 22H7C4 17 4 7 10 1zM7 23l-5 6 4-1M13 23l5 6-4-1"/><circle cx="10" cy="11" r="2.5"/></svg>
    <h4>Market</h4><p>Between SEO, SEM, social, blogging, &amp; email, web marketing can become overwhelming. I help you figure out the right path for growth.</p><a>Read More</a></div>

  <h2 style="left:56px;top:400px">What you'll get</h2>
  <p class="t" style="left:56px;top:437px;width:330px">I want to share our values with you so you can see what it's like working with me.</p>

  <div class="val" style="left:55px;top:498px">
    <svg width="32" height="32" viewBox="0 0 32 32" fill="none" stroke="#fff" stroke-width="1.4"><circle cx="16" cy="16" r="14"/><circle cx="16" cy="9" r="1.5"/><path d="M9 13h14M16 13v7l-4 6M16 20l4 6"/></svg>
    <h5>Assessibility</h5><p>You get my actual cell phone number and are welcome to call me 24/7</p></div>
  <div class="val" style="left:222px;top:498px">
    <svg width="32" height="32" viewBox="0 0 32 32" fill="none" stroke="#fff" stroke-width="1.2"><rect x="8" y="2" width="20" height="12"/><circle cx="18" cy="8" r="3"/><path d="M2 22l8-4h8l-6 3h10l6-5M2 30h16l12-8"/></svg>
    <h5>Affordability</h5><p>No small lettering or big corporations here. I promise to give you the best value..</p></div>
  <div class="val" style="left:410px;top:498px">
    <svg width="32" height="32" viewBox="0 0 32 32" fill="none" stroke="#fff" stroke-width="1.2"><path d="M16 7a8 8 0 0 0-5 14v4h10v-4a8 8 0 0 0-5-14zM12 28h8M16 1v3M5 6l2 2M27 6l-2 2M2 15h3M27 15h3"/></svg>
    <h5>Creativity</h5><p>Struggling with what exactly you need? No problem! I'm here to be your brain.</p></div>
  <div class="val" style="left:594px;top:498px">
    <svg width="32" height="30" viewBox="0 0 32 30" fill="none" stroke="#fff" stroke-width="1.6"><path d="M16 28S2 19 2 10a7 7 0 0 1 14-2 7 7 0 0 1 14 2c0 9-14 18-14 18z"/></svg>
    <h5>Care and Love</h5><p>Yes, I put my sweat tears and energy into my projects and my customers.</p></div>

  <div class="team-photo" role="img" aria-label="Portrait of the agency founder"></div>
  <h2 style="left:290px;top:670px">Our Team</h2>
  <p class="t" style="left:290px;top:706px;width:420px;font-size:10.5px;line-height:14px">Lorem ipsum dolor sit amet, consectetur adipiscing elit, usmod tempor incididunt ut labore et ipsum suspendisse ultrices gravida.</p>
  <div class="avatar" role="img" aria-label="Team member portrait" style="left:290px;top:769px;width:102px;height:102px;background:#4b5ca8"></div>
  <div class="avatar" role="img" aria-label="Team member portrait" style="left:420px;top:755px;width:122px;height:122px;background:var(--blue-light);border:2px solid #fff"></div>
  <div class="avatar" role="img" aria-label="Team member portrait" style="left:582px;top:769px;width:102px;height:102px;background:#2b3a7a"></div>
  <svg class="abs" style="left:709px;top:813px" width="10" height="22" viewBox="0 0 10 22" fill="none" stroke="#2ee08c" stroke-width="1.5"><path d="M1 1l8 10-8 10"/></svg>
</section>

<footer class="footer">
  <div class="fh" style="left:225px;top:38px">ABOUT US</div>
  <p class="ft" style="left:224px;top:72px;width:220px">We are a website and marketing agency. We do website design, development, and well as Brindle and Quorvia advertising and analytics.</p>
  <div class="fh" style="left:224px;top:138px">NEWSLETTER</div>
  <p class="ft" style="left:224px;top:172px;width:220px">Sign up for out monthly newsletter to stay current on all your compliance concerns.</p>
  <div class="abs" style="left:224px;top:207px;font-size:10px;font-weight:700">EMAIL ADDRESS</div>
  <div class="field" style="left:224px;top:231px;width:226px;height:26px;background:#000;color:#fff;font-size:7px">JON.DOE@MAIL.COM</div>
  <div class="btn" style="left:226px;top:276px;width:81px;height:24px;font-size:7px">SUBMIT</div>

  <div class="fh" style="left:518px;top:38px">COMPANY</div>
  <div class="ft" style="left:518px;top:72px;line-height:27.5px">Home<br>Services<br>Portfolio<br>Team</div>
  <div class="fh" style="left:519px;top:199px">CONTACT</div>
  <svg class="abs" style="left:519px;top:237px" width="22" height="22" viewBox="0 0 22 22" fill="none" stroke="#fff" stroke-width="1.4"><circle cx="11" cy="11" r="10"/><rect x="6" y="7.5" width="10" height="7"/><path d="M6 8l5 4 5-4"/></svg>
  <div class="abs" style="left:551px;top:243px;font-size:9px;font-weight:700">info@corvane.example</div>
  <svg class="abs" style="left:519px;top:275px" width="22" height="22" viewBox="0 0 22 22" fill="none" stroke="#fff" stroke-width="1.4"><circle cx="11" cy="11" r="10"/><path d="M7 6l2 0 1 3-1.5 1a7 7 0 0 0 3.5 3.5l1-1.5 3 1v2c-5 1-10-4-9-9z"/></svg>
  <div class="abs" style="left:551px;top:281px;font-size:9px;font-weight:700">555-014-2290</div>

  <div class="fh" style="left:702px;top:38px">Get in Touch</div>
  <div class="abs" style="left:703px;top:79px;font-size:11px">Full name *</div>
  <div class="abs" style="left:849px;top:79px;font-size:11px">Email Address *</div>
  <div class="field" style="left:703px;top:102px;width:125px;height:30px">Full name</div>
  <div class="field" style="left:850px;top:102px;width:125px;height:30px">Email</div>
  <div class="abs" style="left:704px;top:176px;font-size:11px">Message *</div>
  <div class="field" style="left:705px;top:194px;width:270px;height:75px;background:linear-gradient(#fff,#f2f2f2)">Message</div>
  <div class="btn" style="left:705px;top:269px;width:270px;height:30px;font-size:10px">Submit</div>
</footer>

<div class="bottom">
  <div class="abs" style="left:227px;top:22px">© 2021 Corvane . All Rights Reserved</div>
  <div class="soc" style="left:517px"></div>
  <div class="soc" style="left:553px"></div>
  <div class="soc" style="left:589px"></div>
  <div class="soc" style="left:625px"></div>
  <div class="soc" style="left:661px"></div>
  <div class="abs" style="left:826px;top:22px">Privacy Policy &amp; Terms of Service</div>
</div>

</body>
</html>
```